Letterhead for a German Distribution/Manufacturing Company

We need a professional Letterhead in a unique Design.
not to playful.
The Letterhead has to show show that we are a international company with headquater in Germany.
all details like adress, Vat Tax Number, Bank Accout, Eori, email, Company number has to be on the Letterhead.
for example use: VAT TAX DE5704168 Bank Account: Norrfeld Bank IBAN DE421705238ß310482 Swift: KOLV3154802 EORI 3041296587 Company Number: HRB 61508 Adress: VOLTRINA UG Amsel Strasse 7 Postal Code 04683 City Halvenau Country: Germany Email: info@voltrina-example.com
the design can be colored but doesnt have to be
Industry/Entity Type
Manufacturing and international distribution
Requirements
Must have
- show that we are a international company with headquater in Germany. our company infos and logo

```html
<!DOCTYPE html>
<html lang="en">
<head>
<meta charset="utf-8">
<title>VOLTRINA Letterhead</title>
<link href="https://fonts.googleapis.com/css2?family=Figtree:wght@400;500;700&display=swap" rel="stylesheet">
<style>
  :root {
    --canvas: #f2f2f4;
    --paper: #ffffff;
    --header-band: #f0f0f0;
    --ink: #3a3a3a;
    --ink-strong: #1f1f1f;
    --rule: #9a9a9a;
    --watermark: #f3f3f3;
  }
  html, body {
    margin: 0;
    padding: 0;
    width: 1200px;
    height: 1200px;
    overflow: hidden;
    background: var(--canvas);
    font-family: "Figtree", Arial, sans-serif;
  }
  .letterhead {
    position: absolute;
    left: 200px;
    top: 35px;
    width: 800px;
    height: 1130px;
    background: var(--paper);
    box-shadow: 6px 8px 10px rgba(0,0,0,0.35);
  }
  .header-band {
    position: absolute;
    left: 0; top: 0;
    width: 100%;
    height: 172px;
    background: var(--header-band);
    display: flex;
    align-items: center;
    justify-content: center;
  }
  .brand {
    display: flex;
    align-items: center;
    gap: 14px;
    color: var(--ink);
    font-weight: 500;
    font-size: 44px;
    letter-spacing: 1px;
  }
  .brand-dot {
    width: 58px;
    height: 58px;
    border-radius: 50%;
    background: var(--ink);
  }
  .watermark {
    position: absolute;
    left: 0; right: 0;
    top: 500px;
    display: flex;
    align-items: center;
    justify-content: center;
    gap: 26px;
    color: var(--watermark);
    font-weight: 500;
    font-size: 96px;
    letter-spacing: 2px;
  }
  .watermark .brand-dot {
    width: 130px;
    height: 130px;
    background: var(--watermark);
  }
  .footer {
    position: absolute;
    left: 98px;
    right: 98px;
    top: 997px;
    border-top: 1.5px solid var(--rule);
    padding-top: 14px;
    display: grid;
    grid-template-columns: 212px 252px 1fr;
    color: var(--ink-strong);
    font-size: 11px;
    line-height: 1.3;
  }
  .footer-item { margin-bottom: 12px; white-space: nowrap; }
  .footer-label { font-weight: 700; }
</style>
</head>
<body>
  <main class="letterhead">
    <header class="header-band">
      <div class="brand">
        <span class="brand-dot"></span>
        <span class="brand-name">VOLTRINA</span>
      </div>
    </header>

    <div class="watermark" aria-hidden="true">
      <span class="brand-dot"></span>
      <span>VOLTRINA</span>
    </div>

    <footer class="footer">
      <div class="footer-col">
        <div class="footer-item">
          <div class="footer-label">VAT TAX</div>
          <div>DE5704168</div>
        </div>
        <div class="footer-item">
          <div class="footer-label">Address</div>
          <div>VOLTRINA UG Amsel Strasse 7 Postal<br>Code 04683 City Halvenau Germany</div>
        </div>
      </div>
      <div class="footer-col">
        <div class="footer-item">
          <div class="footer-label">Bank Account</div>
          <div>Norrfeld Bank IBAN DE421705238ß310482</div>
        </div>
        <div class="footer-item">
          <div class="footer-label">Swift</div>
          <div>KOLV3154802 EORI 3041296587</div>
        </div>
      </div>
      <div class="footer-col">
        <div class="footer-item">
          <div class="footer-label">Company Number</div>
          <div>HRB 61508</div>
        </div>
        <div class="footer-item">
          <div class="footer-label">Email</div>
          <div>info@voltrina-example.com</div>
        </div>
      </div>
    </footer>
  </main>
</body>
</html>
```